Roof Plumbing Company needs simple, modern business card using the attached logo and below details:

Dean Halloway
Summit Gutters Pty Ltd
ABN: 58 214 937 062
Phone: 0417 286 531
Email: summitgutters@mailbrook.com
Website: summitgutters.com.au

For all of your metal roof plumbing requirements contact Summit Gutters for an obligation free quote - no job too big or to small!

Industry/Entity Type

Business

Contact Information for Business Card

Dean Halloway
Summit Gutters Pty Ltd
ABN 58 214 937 062
0417 286 531
summitgutters@mailbrook.com
summitgutters.com.au

Requirements
Must have
• Bright eye catching design, professional look

```html
<!DOCTYPE html>
<html lang="en">
<head>
<meta charset="utf-8">
<title>Summit Gutters Pty Ltd – Business Card</title>
<link href="https://fonts.googleapis.com/css2?family=Lato:wght@400;700;900&display=swap" rel="stylesheet">
<style>
  :root {
    --bg: #e9e6e2;
    --paper: #ffffff;
    --red: #c0202a;
    --red-deep: #8e1219;
    --red-bright: #d9353b;
    --charcoal: #3a3b3d;
    --grey: #6b6c6e;
    --rule: #c9c9c9;
    --ink: #2f2f31;
  }
  * { box-sizing: border-box; margin: 0; padding: 0; }
  html, body { width: 1200px; height: 1023px; overflow: hidden; }
  body {
    background: var(--bg);
    font-family: "Lato", sans-serif;
    display: flex;
    flex-direction: column;
    align-items: center;
    justify-content: center;
    gap: 60px;
  }
  .card {
    position: relative;
    width: 700px;
    height: 400px;
    border-radius: 14px;
    overflow: hidden;
    box-shadow: 0 10px 28px rgba(0,0,0,.18);
  }

  /* Front */
  .card--front { background: var(--paper); }
  .front__brand {
    position: absolute;
    left: 50px; top: 0; width: 300px; height: 355px;
    display: flex; align-items: center; justify-content: center;
  }
  .brand-name {
    font-weight: 900;
    font-size: 34px;
    line-height: 1.1;
    color: var(--red);
    text-transform: uppercase;
    letter-spacing: 1px;
    text-align: center;
  }
  .front__divider {
    position: absolute;
    left: 370px; top: 70px; width: 1px; height: 220px;
    background: var(--rule);
  }
  .front__details {
    position: absolute;
    left: 395px; top: 82px;
  }
  .person-name { font-weight: 700; font-size: 27px; color: var(--red); }
  .abn { font-size: 14px; color: var(--grey); margin-top: 2px; }
  .contact-list { list-style: none; margin-top: 38px; }
  .contact-list li {
    display: flex; align-items: center; gap: 12px;
    font-size: 19px; color: var(--ink);
    margin-bottom: 10px;
  }
  .contact-icon { width: 20px; height: 20px; flex: none; }
  .front__band {
    position: absolute; left: 0; bottom: 0; width: 100%; height: 45px;
  }

  /* Back */
  .card--back {
    background: linear-gradient(135deg, var(--red-deep) 0%, var(--red) 50%, var(--red-bright) 100%);
    color: #fff;
  }
  .back__brand {
    position: absolute; left: 0; top: 70px; width: 100%;
    display: flex; align-items: center; justify-content: center;
  }
  .back__brand .brand-name { color: #fff; font-size: 48px; }
  .tagline {
    position: absolute; left: 40px; right: 40px; bottom: 48px;
    font-size: 17px; line-height: 1.5; text-align: center;
  }
</style>
</head>
<body>

<section class="card card--front" aria-label="Business card front">
  <div class="front__brand">
    <p class="brand-name">Summit Gutters<br>Pty Ltd</p>
  </div>
  <div class="front__divider"></div>
  <div class="front__details">
    <p class="person-name">Dean Halloway</p>
    <p class="abn">ABN: 58 214 937 062</p>
    <ul class="contact-list">
      <li>
        <svg class="contact-icon" viewBox="0 0 20 20" aria-hidden="true"><rect x="1" y="3" width="18" height="15" rx="3" fill="var(--red)"/><rect x="5" y="7" width="10" height="7" rx="1" fill="#fff"/></svg>
        0417 286 531
      </li>
      <li>
        <svg class="contact-icon" viewBox="0 0 20 20" aria-hidden="true"><rect x="1" y="4" width="18" height="13" rx="1.5" fill="var(--red)"/><path d="M2 5l8 6 8-6" stroke="#fff" stroke-width="1.6" fill="none"/></svg>
        summitgutters@mailbrook.com
      </li>
      <li>
        <svg class="contact-icon" viewBox="0 0 20 20" aria-hidden="true"><rect x="2" y="3" width="16" height="12" rx="1" fill="none" stroke="var(--red)" stroke-width="2"/><rect x="7" y="16" width="6" height="2" fill="var(--red)"/></svg>
        summitgutters.com.au
      </li>
    </ul>
  </div>
  <svg class="front__band" viewBox="0 0 700 45" preserveAspectRatio="none" aria-hidden="true">
    <polygon points="0,0 470,0 440,45 0,45" fill="var(--red)"/>
    <polygon points="470,0 700,0 700,45 440,45" fill="var(--charcoal)"/>
  </svg>
</section>

<section class="card card--back" aria-label="Business card back">
  <div class="back__brand">
    <p class="brand-name">Summit Gutters<br>Pty Ltd</p>
  </div>
  <p class="tagline">For all of your metal roof plumbing requirements contact Summit Gutters<br>for an obligation free quote - no job too big or to small!</p>
</section>

</body>
</html>
```